Webpage Design_Telecommunications VOIP

BRV Linkworks Inc. Talk Made Simple.
Webpage/Homepage Design for Voiceover IP solution and Telecommunications company, looking to expand market and compete with larger providers.
He has a long standing local provider business with http://www.harborlane-example.com/ (You can see the logo there, blue cloud, phone pad) with tag Line: Communications Evolved in first rotation. You can also find layout and content for voiceover IP services, which is the focus for BRV Linkworks, so it can stand alone from Harborlane.

Target Market(s)

Malls, Doctors Offices, Retail, Hospitals, Car Dealers, Finance Services, HR Services, Insurance, Hotels, Travel Commerce, Government, Software Companies, Large Health Clubs/Country Clubs, Entertainment Venues, Quarrow Arena, Maplecrest Pines University/Colleges/Education.
See Product list on Talo (also Site inspiration) they set their site up based on different verticals, just to give you some inspiration.
http://talo-example.com/small-business/
http://talo-example.com/government/

Industry/Entity Type

Telecommunications

Number of Pages Required

1 page

Font styles to use
Sans Serif

Requirements
Must have
• Logo, Clean, Simple Strong Highlight services Navigation.
• Similar, competitive and current design like http://talo-example.com/
• Strong theme of Customer Service, but with modern competitive messaging.
• Fast, simple communication solutions/messages.
• Use of the Phone in the cloud graphic as an interactive feature.
• Contact form
• Pixelvault Image ID: 508342716
• Image ID: 634910275
• Image ID: 172605943
Nice to have
• Quick Service boxes for "PRICING" (to be supported with a smart form on our end)
Should not have
• Generic Images, of Professionals shaking hands, please chose images less expected.

```html
<!DOCTYPE html>
<html lang="en">
<head>
<meta charset="utf-8">
<title>BRV Linkworks – Talk Made Simple</title>
<link href="https://fonts.googleapis.com/css2?family=Nunito+Sans:wght@400;600;700;800;900&family=Open+Sans:wght@400;600;700&display=swap" rel="stylesheet">
<style>
:root{
  --brand-blue:#2aa5de;
  --nav-blue:#45b1e3;
  --nav-active:#1c86c8;
  --deep-blue:#0f6dac;
  --sky:#3fb0e4;
  --ink:#1f1f1f;
  --muted:#444;
  --page-bg:#ececec;
  --field:#cfcfcf;
  --white:#ffffff;
}
*{box-sizing:border-box;margin:0;padding:0}
html,body{width:1200px;height:2723px;overflow:hidden}
body{background:var(--page-bg);font-family:"Open Sans",Arial,sans-serif;color:var(--ink);position:relative}
.abs{position:absolute}
.sheet{position:absolute;left:15px;top:0;width:1170px;height:2646px;background:var(--white);box-shadow:0 6px 10px rgba(0,0,0,.18)}
.heading{font-family:"Nunito Sans",Arial,sans-serif;font-weight:800;text-transform:uppercase}

/* header */
.ribbon{left:645px;top:22px;width:540px;height:42px;background:var(--brand-blue);clip-path:polygon(0 0,100% 0,100% 100%,42px 100%);color:#fff;font-family:"Nunito Sans",sans-serif;font-weight:800;font-size:17.5px;line-height:42px;padding-left:72px;letter-spacing:.2px}
.topline{left:15px;top:22px;width:640px;height:4px;background:var(--brand-blue)}
.logo{display:flex;align-items:center;gap:14px}
.logo-dot{width:50px;height:50px;border-radius:50%;background:var(--brand-blue)}
.logo-name{font-family:"Nunito Sans",sans-serif;font-weight:800;font-size:40px;color:var(--ink);line-height:1}
.logo-tag{font-size:14px;color:var(--ink);margin-top:2px;letter-spacing:.5px}
.header-logo{left:36px;top:62px}
.call{left:886px;top:90px;display:flex;gap:12px;align-items:flex-start}
.call-label{font-family:"Nunito Sans",sans-serif;font-weight:700;font-size:16.5px;color:var(--ink);line-height:1}
.call-number{font-family:"Nunito Sans",sans-serif;font-weight:700;font-size:34px;color:var(--brand-blue);line-height:1.05}

/* nav */
.nav{left:15px;top:169px;width:1170px;height:45px;background:var(--nav-blue)}
.nav-item{position:absolute;top:0;height:45px;line-height:45px;transform:translateX(-50%);color:#fff;font-family:"Nunito Sans",sans-serif;font-weight:800;font-size:18.5px;text-transform:uppercase}
.nav-active{position:absolute;left:0;top:0;width:161px;height:45px;background:var(--nav-active)}

/* hero */
.hero{left:15px;top:214px;width:1170px;height:445px;background:linear-gradient(100deg,#e9ecef 0%,#c9cfd6 30%,#3b3f45 48%,#2b2e33 60%,#cfd4da 78%,#eef0f2 100%)}
.dots{left:571px;top:639px;display:flex;gap:9px}
.dots span{width:7px;height:7px;border-radius:50%;background:#fff;opacity:.8}
.dots span:first-child{background:var(--brand-blue);opacity:1}

/* intro */
.intro{left:15px;top:659px;width:1170px;height:205px;background:var(--deep-blue);color:#fff;text-align:center}
.intro p{position:absolute;left:55px;width:1060px;top:22px;font-size:17.5px;line-height:23.6px}
.btn-outline{position:absolute;height:40px;border:2px solid #fff;border-radius:5px;color:#fff;font-family:"Nunito Sans",sans-serif;font-weight:800;font-size:16px;line-height:36px;text-align:center;text-transform:uppercase}
.intro .btn-outline{left:506px;top:141px;width:158px}
.band-shadow{left:60px;top:864px;width:1080px;height:16px;background:radial-gradient(ellipse at top,rgba(0,0,0,.22),rgba(0,0,0,0) 70%)}

/* section titles */
.section-title{width:1200px;left:0;text-align:center;font-size:26px;letter-spacing:.3px}

/* services */
.service{width:230px;transform:translateX(-50%);text-align:center;top:958px}
.service-icon{width:131px;height:131px;border-radius:50%;background:var(--brand-blue);margin:0 auto;display:flex;align-items:center;justify-content:center}
.service-name{margin-top:20px;font-size:20px;font-family:"Nunito Sans",sans-serif;font-weight:800}
.service-text{margin-top:6px;font-size:13px;line-height:16.5px;font-weight:600;color:var(--muted)}
.btn-dark{left:521px;top:1258px;width:158px;height:42px;border:2px solid var(--ink);border-radius:5px;font-family:"Nunito Sans",sans-serif;font-weight:800;font-size:16px;line-height:38px;text-align:center;text-transform:uppercase}

/* solutions */
.solutions{left:15px;top:1334px;width:1170px;height:434px;background:linear-gradient(180deg,#5ec0ea 0%,#3aaee2 50%,#2ea4dc 100%)}
.solutions .section-title{left:-15px;top:34px;color:#fff}
.solution{width:200px;transform:translateX(-50%);text-align:center;color:#fff}
.solution-name{font-family:"Nunito Sans",sans-serif;font-weight:700;font-size:16px;text-transform:uppercase}
.solution-text{font-size:12.5px;line-height:16px;font-weight:600}
.caret{display:block;margin:6px auto}
.solutions .btn-outline{left:506px;top:360px;width:158px}

/* partners */
.partner{transform:translate(-50%,-50%);font-family:"Nunito Sans",sans-serif;font-weight:900;font-size:38px;color:var(--deep-blue);top:1897px}
.arrow{top:1884px}

/* news */
.news{left:15px;top:1970px;width:1170px;height:317px;background:linear-gradient(90deg,#3ca9df 0%,#6fc3ea 45%,#3aaae0 100%)}
.news .section-title{left:-15px;top:34px;color:#fff}
.news-photo{width:136px;height:136px;top:92px}
.news-date{top:102px;font-size:13px;font-weight:700;color:#fff}
.news-text{top:132px;width:312px;font-size:12.5px;line-height:16.5px;font-weight:600;color:#fff}
.read-more{top:253px;width:151px;height:30px;border:2px solid #fff;border-radius:15px;color:#fff;font-family:"Nunito Sans",sans-serif;font-weight:800;font-size:13px;line-height:26px;padding-left:12px;text-transform:uppercase}
.read-more svg{position:absolute;right:12px;top:8px}

/* contact */
.contact-title{top:2326px;font-size:26px}
.contact-logo{left:80px;top:2400px}
.contact-logo .logo-dot{width:34px;height:34px}
.contact-logo .logo-name{font-size:27px}
.contact-logo .logo-tag{font-size:10px}
.contact-line{left:80px;display:flex;gap:14px;align-items:flex-start;font-size:15px;font-weight:600;line-height:22px}
.contact-line svg{margin-top:4px;flex:none}
.social{left:104px;top:2604px;display:flex;gap:12px}
.social span{width:16px;height:16px;border-radius:50%;background:var(--brand-blue)}
.field{background:var(--field);font-size:13px;font-weight:600;color:#333;padding:8px 18px;height:37px}
.send{left:824px;top:2479px;width:103px;height:37px;background:#111;color:#fff;font-family:"Nunito Sans",sans-serif;font-weight:800;font-size:14px;line-height:37px;text-align:center}
.copyright{left:0;top:2664px;width:1200px;text-align:center;font-size:11px;font-weight:700;color:#555;text-transform:uppercase}
</style>
</head>
<body>
<div class="sheet"></div>

<!-- header -->
<div class="abs topline"></div>
<div class="abs ribbon">Communications Evolved in First Rotation</div>
<div class="abs logo header-logo">
  <span class="logo-dot"></span>
  <div>
    <div class="logo-name">BRV Linkworks</div>
    <div class="logo-tag">talk made simple</div>
  </div>
</div>
<div class="abs call">
  <svg width="46" height="46" viewBox="0 0 46 46" aria-hidden="true"><circle cx="23" cy="23" r="21" fill="none" stroke="#2aa5de" stroke-width="3"/><path d="M15 13c2-2 4-1 5 1l2 4c1 2 0 3-1 4 1 3 3 5 6 6 1-1 2-2 4-1l4 2c2 1 3 3 1 5-3 3-8 2-13-3s-6-10-3-13z" fill="#2aa5de" transform="translate(-1 -1) scale(.95)"/></svg>
  <div>
    <div class="call-label">CALL FOR A FREE CONSULTATION</div>
    <div class="call-number">800.555.0148</div>
  </div>
</div>

<!-- navigation -->
<nav class="abs nav">
  <div class="nav-active"></div>
  <div class="nav-item" style="left:80px">Home</div>
  <div class="nav-item" style="left:237px">About Us</div>
  <div class="nav-item" style="left:392px">Services</div>
  <div class="nav-item" style="left:555px">Solutions</div>
  <div class="nav-item" style="left:720px">Partners</div>
  <div class="nav-item" style="left:878px">BRV News</div>
  <div class="nav-item" style="left:1049px">Contact Us</div>
</nav>

<!-- hero -->
<div class="abs hero" role="img" aria-label="Office desk phone with coiled handset in front of a bright city skyline"></div>
<div class="abs dots"><span></span><span></span><span></span><span></span></div>

<!-- intro -->
<section class="abs intro">
  <p>BRV Linkworks was founded in Brookhollow, MA in 1991 by Dario Vance. Since then we have been focused on providing the businesses in our region with the best equipment and the best service. In our history in business, we have learned a lot about how to deliver reliable systems and services to our customers. Today we are a full service provider of cutting edge business communication systems and services for small and medium businesses.</p>
  <div class="btn-outline">Discover More</div>
</section>
<div class="abs band-shadow"></div>

<!-- services -->
<h2 class="abs heading section-title" style="top:899px">Services</h2>

<div class="abs service" style="left:140px">
  <div class="service-icon"><svg width="70" height="60" viewBox="0 0 70 60" fill="none" stroke="#fff" stroke-width="4"><path d="M8 22c8-10 46-10 54 0v6H8z" fill="#fff"/><rect x="14" y="32" width="42" height="14" rx="3"/><circle cx="24" cy="39" r="2" fill="#fff"/><circle cx="35" cy="39" r="2" fill="#fff"/><circle cx="46" cy="39" r="2" fill="#fff"/><path d="M20 46v8M50 46v8"/></svg></div>
  <div class="service-name">CARRIER</div>
  <div class="service-text">Lorem ipsum dolor sit amet, consectetuer adipiscing elit, sed diam nonummy nibh euismod tincidunt ut laoreet dolore magna aliquam erat volutpat.</div>
</div>
<div class="abs service" style="left:370px">
  <div class="service-icon"><svg width="70" height="70" viewBox="0 0 70 70" fill="none" stroke="#fff" stroke-width="3.5"><circle cx="35" cy="35" r="24"/><ellipse cx="35" cy="35" rx="10" ry="24"/><path d="M11 35h48M15 23h40M15 47h40"/></svg></div>
  <div class="service-name">MANAGED SERVICES</div>
  <div class="service-text">Lorem ipsum dolor sit amet, consectetuer adipiscing elit, sed diam nonummy nibh euismod tincidunt ut laoreet dolore magna aliquam erat volutpat.</div>
</div>
<div class="abs service" style="left:601px">
  <div class="service-icon"><svg width="70" height="70" viewBox="0 0 70 70" fill="none" stroke="#fff" stroke-width="4" stroke-linejoin="round"><path d="M50 8l10 10-8 8-7-5c-6 4-14 12-19 19l5 7-8 8-10-10C14 32 32 14 50 8z"/></svg></div>
  <div class="service-name">KESTREL PHONE</div>
  <div class="service-text">Lorem ipsum dolor sit amet, consectetuer adipiscing elit, sed diam nonummy nibh euismod tincidunt ut laoreet dolore magna aliquam erat volutpat.</div>
</div>
<div class="abs service" style="left:829px">
  <div class="service-icon"><svg width="64" height="70" viewBox="0 0 64 70" fill="none" stroke="#fff" stroke-width="3.5"><rect x="6" y="8" width="14" height="54" rx="4"/><rect x="22" y="14" width="36" height="48" rx="3"/><rect x="28" y="20" width="24" height="10" fill="#fff"/><g fill="#fff" stroke="none"><rect x="28" y="36" width="6" height="5"/><rect x="37" y="36" width="6" height="5"/><rect x="46" y="36" width="6" height="5"/><rect x="28" y="45" width="6" height="5"/><rect x="37" y="45" width="6" height="5"/><rect x="46" y="45" width="6" height="5"/></g></svg></div>
  <div class="service-name">CORVANA IP OFFICE</div>
  <div class="service-text">Lorem ipsum dolor sit amet, consectetuer adipiscing elit, sed diam nonummy nibh euismod tincidunt ut laoreet dolore magna aliquam erat volutpat.</div>
</div>
<div class="abs service" style="left:1060px">
  <div class="service-icon"><svg width="70" height="70" viewBox="0 0 70 70" fill="none" stroke="#fff" stroke-width="4" stroke-linecap="round"><path d="M48 18c-14 0-32 2-32 12s32 6 32 16-16 12-30 12"/><rect x="46" y="10" width="14" height="14" rx="2" fill="#fff"/></svg></div>
  <div class="service-name">CABLE</div>
  <div class="service-text">Lorem ipsum dolor sit amet, consectetuer adipiscing elit, sed diam nonummy nibh euismod tincidunt ut laoreet dolore magna aliquam erat volutpat.</div>
</div>
<div class="abs btn-dark">Discover More</div>

<!-- solutions -->
<section class="abs solutions" role="img" aria-label="Blue tinted background of server racks in a data center">
  <h2 class="abs heading section-title">Solutions</h2>

  <div class="abs solution" style="left:121px;top:100px">
    <svg width="104" height="80" viewBox="0 0 104 80" fill="none" stroke="#fff" stroke-width="4"><path d="M8 14h50v32H28l-12 10v-10H8z" fill="#fff"/><path d="M50 6h46v32h-8v10l-12-10H64"/><circle cx="22" cy="30" r="3" fill="#3aaee2" stroke="none"/><circle cx="33" cy="30" r="3" fill="#3aaee2" stroke="none"/><circle cx="44" cy="30" r="3" fill="#3aaee2" stroke="none"/></svg>
    <svg class="caret" width="16" height="9" viewBox="0 0 16 9" fill="none" stroke="#fff" stroke-width="2"><path d="M1 8l7-7 7 7"/></svg>
    <div class="solution-name">Unified Communications</div>
    <div class="solution-text">Lorem ipsum dolor sit amet, consectetuer adipiscing elit, sed diam nonummy nibh.</div>
  </div>

  <div class="abs solution" style="left:333px;top:118px">
    <div class="solution-text">Lorem ipsum dolor sit amet, consectetuer adipiscing elit, sed diam nonummy nibh.</div>
    <div class="solution-name" style="margin-top:8px">Call Center Software</div>
    <svg class="caret" width="16" height="9" viewBox="0 0 16 9" fill="none" stroke="#fff" stroke-width="2"><path d="M1 1l7 7 7-7"/></svg>
    <svg width="80" height="80" viewBox="0 0 80 80" fill="none" stroke="#fff" stroke-width="5"><path d="M14 44V36a26 26 0 0 1 52 0v8"/><rect x="8" y="40" width="14" height="22" rx="5" fill="#fff"/><rect x="58" y="40" width="14" height="22" rx="5" fill="#fff"/><path d="M64 62c0 8-10 12-22 12"/></svg>
  </div>

  <div class="abs solution" style="left:539px;top:100px">
    <svg width="96" height="80" viewBox="0 0 96 80" fill="none" stroke="#fff" stroke-width="3"><path d="M10 40L48 10l38 30M18 34v38h60V34"/><path d="M48 66c-10 0-14-8-10-16 2 4 5 5 6 4-2-8 4-14 8-18 0 8 10 12 8 22-1 5-5 8-12 8z"/></svg>
    <svg class="caret" width="16" height="9" viewBox="0 0 16 9" fill="none" stroke="#fff" stroke-width="2"><path d="M1 8l7-7 7 7"/></svg>
    <div class="solution-name">Disaster Recovery</div>
    <div class="solution-text">Lorem ipsum dolor sit amet, consectetuer adipiscing elit, sed diam nonummy nibh.</div>
  </div>

  <div class="abs solution" style="left:720px;top:118px">
    <div class="solution-text">Lorem ipsum dolor sit amet, consectetuer adipiscing elit, sed diam nonummy nibh.</div>
    <div class="solution-name" style="margin-top:8px">Multisite Offices</div>
    <svg class="caret" width="16" height="9" viewBox="0 0 16 9" fill="none" stroke="#fff" stroke-width="2"><path d="M1 1l7 7 7-7"/></svg>
    <svg width="90" height="70" viewBox="0 0 90 70" fill="none" stroke="#fff" stroke-width="4"><rect x="6" y="4" width="22" height="40" rx="3"/><rect x="36" y="24" width="46" height="28" rx="2"/><path d="M52 62h14M59 52v10"/><rect x="14" y="50" width="16" height="16" rx="2"/></svg>
  </div>

  <div class="abs solution" style="left:893px;top:100px">
    <svg width="90" height="84" viewBox="0 0 90 84" fill="none" stroke="#fff" stroke-width="5"><rect x="8" y="4" width="36" height="74" rx="7"/><circle cx="26" cy="66" r="3" fill="#fff"/><path d="M40 38h36M64 26l14 12-14 12" stroke-linejoin="round"/></svg>
    <svg class="caret" width="16" height="9" viewBox="0 0 16 9" fill="none" stroke="#fff" stroke-width="2"><path d="M1 8l7-7 7 7"/></svg>
    <div class="solution-name">Advanced Mobility</div>
    <div class="solution-text">Lorem ipsum dolor sit amet, consectetuer adipiscing elit, sed diam nonummy nibh.</div>
  </div>

  <div class="abs solution" style="left:1069px;top:118px">
    <div class="solution-text">Lorem ipsum dolor sit amet, consectetuer adipiscing elit, sed diam nonummy nibh.</div>
    <div class="solution-name" style="margin-top:8px">Conferencing</div>
    <svg class="caret" width="16" height="9" viewBox="0 0 16 9" fill="none" stroke="#fff" stroke-width="2"><path d="M1 1l7 7 7-7"/></svg>
    <svg width="90" height="70" viewBox="0 0 90 70" fill="none" stroke="#fff" stroke-width="4"><ellipse cx="45" cy="38" rx="32" ry="14"/><circle cx="45" cy="12" r="7" fill="#fff"/><circle cx="14" cy="50" r="7" fill="#fff"/><circle cx="76" cy="50" r="7" fill="#fff"/><circle cx="45" cy="60" r="7" fill="#fff"/></svg>
  </div>

  <div class="btn-outline">Discover More</div>
</section>

<!-- partners -->
<h2 class="abs heading section-title" style="top:1803px">Partners</h2>
<svg class="abs arrow" style="left:60px" width="14" height="26" viewBox="0 0 14 26" fill="none" stroke="#666" stroke-width="3"><path d="M12 2L2 13l10 11"/></svg>
<div class="abs partner" style="left:209px">Corvana</div>
<div class="abs partner" style="left:454px">Veltrix Networks</div>
<div class="abs partner" style="left:737px">Kestrel</div>
<div class="abs partner" style="left:980px">Tonewell</div>
<svg class="abs arrow" style="left:1125px" width="14" height="26" viewBox="0 0 14 26" fill="none" stroke="#666" stroke-width="3"><path d="M2 2l10 11L2 24"/></svg>

<!-- news -->
<section class="abs news" role="img" aria-label="Soft blue tinted background of a customer support team at work">
  <h2 class="abs heading section-title">BRV News</h2>

  <div class="abs news-photo" style="left:72px;background:linear-gradient(135deg,#1c3f6b,#4f8cc4 60%,#c9d6e4)" role="img" aria-label="Businessman touching a glowing network interface"></div>
  <div class="abs news-date" style="left:232px">December 18, 2015</div>
  <div class="abs news-text" style="left:232px">Lorem ipsum dolor sit amet, consectetuer adipiscing elit, sed diam nonummy nibh euismod tincidunt ut laoreet dolore magna aliquam erat volutpat. Ut wisi enim ad minim veniam, quis nostrud exerci tation ullamcorper.</div>
  <div class="abs read-more" style="left:230px">Read More<svg width="8" height="12" viewBox="0 0 8 12" fill="none" stroke="#fff" stroke-width="2"><path d="M1 1l5 5-5 5"/></svg></div>

  <div class="abs news-photo" style="left:613px;background:linear-gradient(135deg,#e9e4df,#b99a86 55%,#5a4a40)" role="img" aria-label="Smiling support agent wearing a headset"></div>
  <div class="abs news-date" style="left:771px">December 22, 2015</div>
  <div class="abs news-text" style="left:771px">Lorem ipsum dolor sit amet, consectetuer adipiscing elit, sed diam nonummy nibh euismod tincidunt ut laoreet dolore magna aliquam erat volutpat. Ut wisi enim ad minim veniam, quis nostrud exerci tation ullamcorper.</div>
  <div class="abs read-more" style="left:770px">Read More<svg width="8" height="12" viewBox="0 0 8 12" fill="none" stroke="#fff" stroke-width="2"><path d="M1 1l5 5-5 5"/></svg></div>
</section>

<!-- contact -->
<h2 class="abs heading contact-title" style="left:80px">Contact Info</h2>
<div class="abs logo contact-logo">
  <span class="logo-dot"></span>
  <div>
    <div class="logo-name">BRV Linkworks</div>
    <div class="logo-tag">talk made simple</div>
  </div>
</div>
<div class="abs contact-line" style="top:2448px">
  <svg width="12" height="16" viewBox="0 0 12 16"><path d="M6 0a6 6 0 0 1 6 6c0 4-6 10-6 10S0 10 0 6a6 6 0 0 1 6-6z" fill="#222"/><circle cx="6" cy="6" r="2.2" fill="#fff"/></svg>
  <div>42 Tidewell Rd Unit B4<br>Fernbridge, NH 03999</div>
</div>
<div class="abs contact-line" style="top:2514px">
  <svg width="16" height="13" viewBox="0 0 16 13"><path d="M1 4c0-3 14-3 14 0v2h-4V4H5v2H1z" fill="#222"/><rect x="3" y="7" width="10" height="6" rx="1" fill="#222"/></svg>
  <div>(800) 555-0148</div>
</div>
<div class="abs contact-line" style="top:2557px">
  <svg width="16" height="12" viewBox="0 0 16 12"><rect width="16" height="12" fill="#222"/><path d="M1 1l7 6 7-6" fill="none" stroke="#fff" stroke-width="1.4"/></svg>
  <div>sales@harborlane-example.com</div>
</div>
<div class="abs social"><span aria-label="Social profile"></span><span aria-label="Social profile"></span></div>

<h2 class="abs heading contact-title" style="left:514px">Send Us a Message</h2>
<div class="abs field" style="left:514px;top:2383px;width:297px">Name</div>
<div class="abs field" style="left:514px;top:2432px;width:297px">Email</div>
<div class="abs field" style="left:514px;top:2479px;width:297px">Phone</div>
<div class="abs field" style="left:822px;top:2383px;width:300px;height:86px">Message</div>
<div class="abs send">SEND</div>

<div class="abs copyright">Copyright © 2016 BRV Linkworks. All rights reserved.</div>
</body>
</html>
```